'Private English tutoring'

I need a flyer design to advertise private English tutoring. I am offering lessons to ethnic minority groups in my local area in south Belfast. The biggest ethnic minorities groups are Chinese, Polish and Indian and African. I can teach at any level, from beginner English to advanced. The tutoring will be either one on one or small groups of four students. I can teach adults and children but my preference would be to teach adults.

The flyer would need to be easily understood by people who have English as a second language.

I am also offering proof reading and editing services to students at local universities and colleges.

Target Market(s)

Adults of ethnic minorities who may not speak or read much English

Industry/Entity Type

Tutoring

Font styles to use
Serif

Requirements
Must have
• It needs to communicate that I am an accredited TEFL (Teaching English as a Foreign language) tutor with 2 years experience and that I tutor Beginners - Advanced students. It would also need to say that I offer proof reading and editing services. It would also need to communicate the cost of lessons are £15, but there are group rates for groups of 2-4 students. It would need to include my contact details which are as follows: contact Nora Calloway BTh at 07812639504 or email noracallowayenglish@vendrimail.com
Nice to have
• In terms of design I would like it to be warm and inviting and something which would convey an atmosphere of learning for non English speakers. Other than that I don't have any preferences.
Should not have
• Nothing which is going to be offensive to ethnic minorities.
• No pictures of people

```html
<!DOCTYPE html>
<html lang="en">
<head>
<meta charset="utf-8">
<title>Private English Tutoring Flyer</title>
<link rel="stylesheet" href="https://fonts.googleapis.com/css2?family=Montserrat:wght@500;700;800;900&family=Crimson+Pro:ital,wght@0,400;0,600;0,700;1,400&family=Merriweather:wght@700;900&display=swap">
<style>
  :root {
    --backdrop: #c3c1c1;
    --frame-blue: #6fc7e6;
    --line-blue: #7dcbeb;
    --red-top: #df4058;
    --red-bottom: #c32a3d;
    --cream: #f3edb0;
  }
  * { margin: 0; padding: 0; box-sizing: border-box; }
  html, body {
    width: 1200px; height: 960px; overflow: hidden;
    background: var(--backdrop);
  }
  .flyer {
    position: absolute; left: 290px; top: 41px;
    width: 620px; height: 877px;
    background: var(--frame-blue);
    padding: 22px;
  }
  .panel {
    position: relative; width: 576px; height: 833px;
    background: linear-gradient(180deg, var(--red-top), var(--red-bottom));
    overflow: hidden;
  }
  .dividers { position: absolute; inset: 0; }
  .dividers line, .dividers rect { fill: none; stroke: var(--line-blue); stroke-width: 2; }
  .dividers circle { fill: var(--line-blue); }
  .text { position: absolute; left: 0; width: 100%; text-align: center; white-space: nowrap; }
  .sans { font-family: "Montserrat", sans-serif; font-weight: 800; }
  .serif { font-family: "Crimson Pro", serif; }
  .headline { color: var(--cream); line-height: 1; letter-spacing: 2px; }
  .headline-learn { top: 42px; font-size: 118px; }
  .headline-sub { top: 150px; font-size: 46px; font-style: italic; color: var(--line-blue); }
  .headline-english { top: 200px; font-size: 108px; }
  .tutoring-label {
    top: 358px; font-family: "Merriweather", serif; font-weight: 900;
    font-size: 21px; letter-spacing: 1px; color: var(--line-blue);
  }
  .price { top: 420px; font-size: 38px; color: var(--cream); }
  .price .per { font-family: "Crimson Pro", serif; font-weight: 600; font-style: italic; }
  .group-rates { top: 483px; font-size: 28px; color: var(--line-blue); }
  .group-size { top: 515px; font-size: 26px; color: var(--cream); }
  .levels { top: 566px; font-size: 27px; color: var(--cream); }
  .levels .arrow { color: var(--line-blue); }
  .accreditation { top: 626px; font-family: "Montserrat", sans-serif; font-weight: 500; font-size: 18px; color: var(--line-blue); }
  .contact-title { top: 676px; font-size: 32px; color: var(--cream); }
  .contact-name { top: 716px; font-family: "Merriweather", serif; font-weight: 900; font-size: 17px; color: var(--line-blue); }
  .contact-phone { top: 740px; font-family: "Montserrat", sans-serif; font-weight: 800; font-size: 18px; color: var(--line-blue); letter-spacing: 1px; }
  .contact-email { top: 764px; font-family: "Montserrat", sans-serif; font-weight: 700; font-size: 16px; color: var(--line-blue); }
  .services { top: 795px; font-size: 23px; color: var(--cream); }
  .services b { font-weight: 700; }
</style>
</head>
<body>
  <div class="flyer">
    <div class="panel">
      <svg class="dividers" viewBox="0 0 576 833" aria-hidden="true">
        <line x1="188" y1="330" x2="278" y2="330"/>
        <circle cx="288" cy="330" r="4"/>
        <line x1="298" y1="330" x2="388" y2="330"/>
        <rect x="88" y="348" width="400" height="46" rx="4"/>
        <line x1="238" y1="472" x2="338" y2="472"/>
        <line x1="238" y1="557" x2="338" y2="557"/>
        <line x1="238" y1="614" x2="338" y2="614"/>
        <line x1="188" y1="664" x2="278" y2="664"/>
        <circle cx="288" cy="664" r="4"/>
        <line x1="298" y1="664" x2="388" y2="664"/>
        <rect x="12" y="793" width="552" height="32" rx="4"/>
      </svg>

      <div class="text sans headline headline-learn">LEARN</div>
      <div class="text serif headline-sub">to speak &amp; write in</div>
      <div class="text sans headline headline-english">ENGLISH</div>

      <div class="text tutoring-label">PRIVATE ENGLISH TUTORING</div>
      <div class="text sans price">£15 <span class="per">per</span> LESSON</div>

      <div class="text sans group-rates">GROUP RATES</div>
      <div class="text serif group-size">for groups of 2-4</div>
      <div class="text serif levels">tutoring beginners <span class="arrow">→</span> advanced students</div>
      <div class="text accreditation">accredited TEFL tutor with 2 years experience</div>

      <div class="text sans contact-title">CONTACT</div>
      <div class="text contact-name">Nora Calloway BTh</div>
      <div class="text contact-phone">07812639504</div>
      <div class="text contact-email">noracallowayenglish@vendrimail.com</div>

      <div class="text serif services">Nora also offers <b>proof reading</b> and <b>editing</b> services.</div>
    </div>
  </div>
</body>
</html>
```